Box and Paper Bag Design
for exclusive line of prescriptions creams
Box and Paper Bag Design  - Health
Creative Brief
A design for the box (layout attached) and a promotional paper bag (no layout - see sample picture: 8" length, 7" high, 3.5" deep) - front and back designs will be fine. Both packages are for exclusive line of prescription creams. Should resemble expensive, high end, sophisticated and upscale style, yet THIS IS PRESCRIPTION MEDICATION - the packaging should resemble this also. FRONT: 1. Logo (attached) 2. Text: Professional Prescription Formula Dispensed Only By Physicians 3. On the bottom: e 30 ml / 1 fl.oz. Made in USA BACK: All the way on the bottom - try to fit into lower 1/4th of the space: Directions: Follow the directions of your prescribing Physician Cautions: For external use only - do not ingest. Avoid contact with open wounds. Avoid getting into eyes. Make sure skin is clean and dry before applying . Discontinue use if rash or discomfort occurs. Not for use by pregnant or lactating women. The packaging is NOT child resistant. KEEP AWAY FROM CHILDREN. If accidentally ingested seek medical help immediately. _________________________ We will be using various technics while printing the boxes: uv coating, spot foil etc See several samples of the designs I liked attached. Try to stick to conservative yet fresh colors: metallic, silver, gray , blue, green.
Health
Doctors, medical professionals and their patients.

```html
<!DOCTYPE html>
<html lang="en">
<head>
<meta charset="utf-8">
<title>Lumara by DR – Box Dieline</title>
<link href="https://fonts.googleapis.com/css2?family=Questrial&display=swap" rel="stylesheet">
<style>
  :root{
    --stage:#3a3a3a;
    --paper:#ffffff;
    --mist:#cfeef1;
    --aqua:#bfe6ea;
    --accent:#3fbccb;
    --ink:#4a4a4a;
    --ink-soft:#6a6a6a;
    --edge:#9fb4b7;
  }
  *{margin:0;padding:0;box-sizing:border-box}
  html,body{width:1200px;height:961px;overflow:hidden;background:var(--stage)}
  body{position:relative;font-family:"Questrial",sans-serif;color:var(--ink)}
  .dieline{position:absolute;left:0;top:0;width:1200px;height:961px}
  .copy{position:absolute}
  .brand{position:absolute;width:118px;color:var(--ink);font-weight:400;line-height:1;overflow:hidden;text-align:left;white-space:nowrap}
  .brand .word{display:block;font-size:20px;letter-spacing:4px}
  .brand .by{display:block;font-size:12px;letter-spacing:4px;margin-top:12px}
  .brand--lid{left:260px;top:160px;transform:rotate(180deg)}
  .brand--side{left:140px;top:380px}
  .brand--front{left:648px;top:380px}
  .claim{left:640px;top:532px;width:180px;text-align:center;font-size:17px;line-height:1.22;color:var(--ink)}
  .footer-line{position:absolute;top:737px;font-size:10.5px;color:var(--accent)}
  .footer-line--origin{left:646px}
  .footer-line--volume{right:332px}
  .directions{width:236px;font-size:10.6px;line-height:1.26;color:var(--ink-soft);text-align:justify}
  .directions .label{color:var(--accent)}
  .directions--back{left:391px;top:556px}
  .directions--side{left:885px;top:556px}
</style>
</head>
<body>
<svg class="dieline" viewBox="0 0 1200 961" xmlns="http://www.w3.org/2000/svg">
  <defs>
    <linearGradient id="panelFade" x1="0" y1="0" x2="0" y2="1">
      <stop offset="0" stop-color="#ffffff"/>
      <stop offset="0.55" stop-color="#f4fbfc"/>
      <stop offset="1" stop-color="#c9ebee"/>
    </linearGradient>
    <linearGradient id="stripeTone" x1="0" y1="0" x2="1" y2="0">
      <stop offset="0" stop-color="#8f9596"/>
      <stop offset="0.5" stop-color="#c4c8c9"/>
      <stop offset="1" stop-color="#ffffff" stop-opacity="0"/>
    </linearGradient>
    <linearGradient id="stripeToneV" x1="0" y1="0" x2="0" y2="1">
      <stop offset="0" stop-color="#9aa0a1"/>
      <stop offset="1" stop-color="#ffffff" stop-opacity="0"/>
    </linearGradient>
  </defs>

  <path class="lid-tab" d="M125 104 V82 Q125 47 160 47 H350 Q385 47 385 82 V104 Z" fill="var(--paper)"/>
  <rect class="lid-panel" x="125" y="104" width="260" height="229" fill="url(#panelFade)"/>
  <rect class="lid-texture" role="img" aria-label="Fine silver vertical line texture" x="125" y="104" width="150" height="229" fill="url(#stripeTone)" opacity="0.7"/>
  <rect x="255" y="122" width="126" height="130" fill="var(--paper)"/>

  <polygon class="dust-flap" points="385,333 400,262 620,262 632,333" fill="var(--paper)"/>
  <polygon class="dust-flap" points="879,333 892,262 1112,262 1125,333" fill="var(--paper)"/>

  <rect class="panel panel--side" x="125" y="333" width="260" height="425" fill="url(#panelFade)"/>
  <rect class="panel panel--back" x="385" y="333" width="247" height="425" fill="url(#panelFade)"/>
  <rect class="panel panel--front" x="632" y="333" width="247" height="425" fill="url(#panelFade)"/>
  <rect class="panel panel--side" x="879" y="333" width="246" height="425" fill="url(#panelFade)"/>

  <rect role="img" aria-label="Fine silver vertical line texture" x="160" y="333" width="220" height="180" fill="url(#stripeToneV)" opacity="0.45"/>
  <path role="img" aria-label="Silver hourglass line texture" d="M385 333 H632 L560 440 H457 Z" fill="url(#stripeToneV)" opacity="0.75"/>
  <path role="img" aria-label="Silver hourglass line texture" d="M879 333 H1125 L1053 440 H951 Z" fill="url(#stripeToneV)" opacity="0.75"/>
  <rect role="img" aria-label="Fine silver vertical line texture" x="760" y="336" width="116" height="160" fill="url(#stripeTone)" opacity="0.6" transform="translate(1636 0) scale(-1 1)"/>
  <rect x="640" y="340" width="116" height="152" fill="var(--paper)"/>

  <rect class="footer-band" x="632" y="732" width="247" height="26" fill="var(--aqua)"/>

  <polygon class="dust-flap" points="385,758 632,758 617,832 400,832" fill="var(--mist)"/>
  <polygon class="dust-flap" points="879,758 1125,758 1110,832 894,832" fill="var(--mist)"/>
  <path class="base-flap" d="M632 758 H879 V896 Q879 926 849 926 H662 Q632 926 632 896 Z" fill="var(--aqua)"/>

  <g stroke="var(--edge)" stroke-width="0.8" fill="none">
    <line x1="125" y1="333" x2="1125" y2="333"/>
    <line x1="125" y1="758" x2="1125" y2="758"/>
    <line x1="385" y1="333" x2="385" y2="758"/>
    <line x1="632" y1="333" x2="632" y2="758"/>
    <line x1="879" y1="333" x2="879" y2="758"/>
    <line x1="125" y1="104" x2="385" y2="104"/>
  </g>
</svg>

<div class="brand brand--lid"><span class="word">LUMARA</span><span class="by">BY DR</span></div>
<div class="brand brand--side"><span class="word">LUMARA</span><span class="by">BY DR</span></div>
<div class="brand brand--front"><span class="word">LUMARA</span><span class="by">BY DR</span></div>

<p class="copy claim">Professional Prescription Formula Dispensed Only By Physicians</p>
<span class="footer-line footer-line--origin">Made in USA</span>
<span class="footer-line footer-line--volume">e 30 ml / 1 fl.oz.</span>

<p class="copy directions directions--back"><span class="label">Directions:</span> Follow the directions of your prescribing Physician.<br><span class="label">Cautions:</span> For external use only - do not ingest. Avoid contact with open wounds. Avoid getting into eyes. Make sure skin is clean and dry before applying. Discontinue use if rash or discomfort occurs. Not for use by pregnant or lactating women. The packaging is NOT child resistant. KEEP AWAY FROM CHILDREN. If accidentally ingested seek medical help immediately.</p>
<p class="copy directions directions--side"><span class="label">Directions:</span> Follow the directions of your prescribing Physician.<br><span class="label">Cautions:</span> For external use only - do not ingest. Avoid contact with open wounds. Avoid getting into eyes. Make sure skin is clean and dry before applying. Discontinue use if rash or discomfort occurs. Not for use by pregnant or lactating women. The packaging is NOT child resistant. KEEP AWAY FROM CHILDREN. If accidentally ingested seek medical help immediately.</p>
</body>
</html>
```